Change logo on company documents

I want to change the logo on all company documents and change them company name that is written in certain places in the text.

Target Market(s)

Construction/Residential Home Remodeling

Colors

Designer to choose colors to be used in the design.

```html
<!DOCTYPE html>
<html lang="en">
<head>
<meta charset="utf-8">
<title>Proposal Estimate</title>
<link rel="stylesheet" href="https://fonts.googleapis.com/css2?family=Arimo:wght@400;700&family=Open+Sans:wght@400&display=swap">
<style>
  :root{
    --ink:#000;
    --paper:#fff;
    --rule:#1a1a1a;
    --header-fill:#f2f2f2;
    --page-edge:#555;
    --address-ink:#222;
  }
  *{box-sizing:border-box;margin:0;padding:0}
  html,body{width:910px;height:1200px;overflow:hidden;background:var(--paper)}
  body{font-family:"Arimo",Arial,sans-serif;color:var(--ink)}
  .sheet{position:relative;width:910px;height:1200px;border:1px solid var(--page-edge);margin:0}
  .brand{position:absolute;left:62px;top:52px;width:125px;display:flex;flex-direction:column;align-items:center;gap:8px}
  .brand-dot{width:56px;height:56px;border:5px solid var(--ink);border-radius:50%}
  .brand-name{font-family:"Arimo",Arial,sans-serif;font-weight:700;font-size:17px;line-height:1.1;text-align:center;letter-spacing:.5px;color:var(--ink)}
  .doc-title{position:absolute;left:205px;top:134px;font-size:29px;font-weight:700;letter-spacing:.2px}
  .company-address{position:absolute;right:71px;top:44px;text-align:right;font-family:"Open Sans",Arial,sans-serif;font-size:15px;line-height:21.5px;letter-spacing:1.1px;color:var(--address-ink)}
  table{border-collapse:collapse;table-layout:fixed;position:absolute}
  td,th{border:1.5px solid var(--rule);height:29px;font-size:16px;text-align:left;padding:0 0 0 9px;font-weight:400;white-space:nowrap}
  .proposal-info{left:37px;top:190px;width:837px}
  .proposal-info .header-row td{background:var(--header-fill);font-weight:700}
  .section-heading{position:absolute;font-size:17.5px;font-weight:700}
  .heading-estimate{left:36px;top:323px}
  .heading-scope{left:31px;top:610px}
  .estimate-lines{left:61px;top:357px;width:788px}
  .estimate-lines th{background:var(--ink);color:var(--paper);font-weight:700;border-color:var(--ink)}
  .estimate-lines .grand-total td.label{font-weight:700}
  .estimate-lines td.label{padding-left:9px}
  .scope-box{position:absolute;left:37px;top:639px;width:839px;height:525px;border:2px solid var(--ink)}
</style>
</head>
<body>
<div class="sheet">
  <div class="brand">
    <div class="brand-dot"></div>
    <div class="brand-name">HARBOR<br>OAK</div>
  </div>

  <h1 class="doc-title">PROPOSAL ESTIMATE</h1>

  <address class="company-address" style="font-style:normal">
    400 CYPRESS LANDING DRIVE<br>
    SUITE 210<br>
    RIVERBEND, LA 70999<br>
    P:&nbsp; 555.014.2260<br>
    F:&nbsp; 555.014.2261
  </address>

  <table class="proposal-info">
    <colgroup><col style="width:145px"><col style="width:273px"><col style="width:145px"><col></colgroup>
    <tr class="header-row"><td>Proposal #</td><td></td><td>Date</td><td></td></tr>
    <tr><td>Proposal For</td><td></td><td>Project / Job</td><td></td></tr>
    <tr><td>Representative</td><td></td><td>Contact</td><td></td></tr>
    <tr><td>Email</td><td></td><td></td><td></td></tr>
  </table>

  <h2 class="section-heading heading-estimate">DETAILED ESTIMATE</h2>

  <table class="estimate-lines">
    <colgroup><col style="width:57px"><col style="width:353px"><col style="width:65px"><col style="width:72px"><col style="width:121px"><col></colgroup>
    <tr><th>Item</th><th>Description of Work</th><th style="padding-left:10px">Qty</th><th>Unit</th><th>Unit Cost</th><th>Line Total</th></tr>
    <tr><td>1</td><td></td><td></td><td></td><td></td><td></td></tr>
    <tr><td>2</td><td></td><td></td><td></td><td></td><td></td></tr>
    <tr><td>3</td><td></td><td></td><td></td><td></td><td></td></tr>
    <tr><td>4</td><td></td><td></td><td></td><td></td><td></td></tr>
    <tr><td></td><td class="label">Subtotal</td><td></td><td></td><td></td><td></td></tr>
    <tr><td></td><td class="label">Tax</td><td></td><td></td><td></td><td></td></tr>
    <tr class="grand-total"><td></td><td class="label">TOTAL ESTIMATE</td><td></td><td></td><td></td><td></td></tr>
  </table>

  <h2 class="section-heading heading-scope">DETAILED SCOPE OF WORK</h2>
  <div class="scope-box"></div>
</div>
</body>
</html>
```